Banner Ad Design Project

I need a banner design. The website is under construction at www.brightmarrowfield.com

Name: Bright Marrow
Tagline: Clear leadership thinking for full calendars

This is a leadership development and executive coaching site. The past site is live at www.quillponderhub.com. (so you can get a sense of the content)

The audience are (BUSY) executives, senior managers, leaders and top professionals, so the feel needs to be highly professional but also modern and fresh. I want to communicate energy but also solid and trust worthy and not too new agey. The audience are also people with strong social values who want to change things - so not too corporate (Ie suits!)

I would like the design to be floating on a white background, very clean and simple. I am attracted to reds or sunset (burn orange crimson colors.) But totally open to any color ideas.
I am giving an open brief for your ideas.
Here are the dimensions 960px wide, roughly 190px height.
Updates

Project Deadline Extended
Reason: The weekend might give more time to designers to get involved. Thanks Mirel

Hi designers

You may not have seen the additions I gave to this brief.

The banner should not have leader out front photo's. Maybe less corporate than I initially thought. 
Not too corporate (no suits!) Please no chess pieces, jigsaw pieces, cartoon images, cliche leadership images. 
Am am trying for inspiration /inspiring whilst still being professional. Very simple and clean.
Please can the design be floating in a white background so that the web page is borderless - A bit like it is in http://tamberwickcove.com/
Thank you

Target Market(s)

Senior managers, executives but people who also want to change the world!

Industry/Entity Type

Construction

Requirements
Should not have
• Should not have leader out front photo's.
Maybe less corporate than I initially thought.
Am am trying for inspiration /inspiring whilst still being professional.
Please no chess pieces, jigsaw pieces, cartoon images, cliche leadership images. Not too corporate (Ie suits!)

Thanks

```html
<!DOCTYPE html>
<html lang="en">
<head>
<meta charset="utf-8">
<title>Bright Marrow — Clear leadership thinking for full calendars</title>
<link rel="stylesheet" href="https://fonts.googleapis.com/css2?family=Tenor+Sans&display=swap">
<style>
  :root {
    --paper: #ffffff;
    --ember: #f2600f;
    --ink: #3a1e14;
    --petal-light: #fbf6ee;
    --petal-mid: #efe4d2;
    --petal-shadow: #d9c9b0;
  }
  html, body {
    margin: 0;
    padding: 0;
    overflow: hidden;
    background: var(--paper);
  }
  .banner {
    position: relative;
    width: 1200px;
    height: 500px;
    overflow: hidden;
    background: var(--paper);
  }
  .light-trails {
    position: absolute;
    inset: 0;
    width: 1200px;
    height: 500px;
  }
  .wordmark {
    position: absolute;
    left: 64px;
    top: 188px;
    width: 500px;
  }
  .brand-name {
    margin: 0;
    font-family: "Tenor Sans", sans-serif;
    font-weight: 400;
    font-size: 56px;
    line-height: 1;
    letter-spacing: 0.5px;
    color: var(--ember);
    white-space: nowrap;
  }
  .tagline {
    margin: 22px 0 0;
    font-family: "Tenor Sans", sans-serif;
    font-size: 16px;
    letter-spacing: 2.4px;
    text-transform: uppercase;
    color: var(--ink);
    white-space: nowrap;
  }
  .bloom {
    position: absolute;
    left: 822px;
    top: 144px;
    width: 232px;
    height: 212px;
    border-radius: 48% 52% 46% 54% / 50% 48% 52% 50%;
    background:
      radial-gradient(circle at 48% 40%, #f4e7c8 0 10%, transparent 24%),
      radial-gradient(circle at 45% 42%, var(--petal-light) 0 38%, var(--petal-mid) 70%, var(--petal-shadow) 100%);
    box-shadow: 0 0 26px 6px rgba(247, 164, 106, 0.35);
  }
</style>
</head>
<body>
  <div class="banner">
    <svg class="light-trails" viewBox="0 0 1200 500" aria-hidden="true">
      <defs>
        <filter id="trail-blur" x="-20%" y="-200%" width="140%" height="500%">
          <feGaussianBlur stdDeviation="9"/>
        </filter>
        <filter id="haze-blur" x="-20%" y="-200%" width="140%" height="500%">
          <feGaussianBlur stdDeviation="22"/>
        </filter>
        <linearGradient id="upper-trail" x1="0" x2="1" y1="0" y2="0">
          <stop offset="0" stop-color="#f7a46a" stop-opacity="0"/>
          <stop offset="0.35" stop-color="#f7a46a" stop-opacity="0.45"/>
          <stop offset="0.6" stop-color="#f2600f" stop-opacity="0.6"/>
          <stop offset="0.82" stop-color="#f7a46a" stop-opacity="0.35"/>
          <stop offset="1" stop-color="#f7a46a" stop-opacity="0"/>
        </linearGradient>
        <linearGradient id="lower-trail" x1="0" x2="1" y1="0" y2="0">
          <stop offset="0" stop-color="#f7a46a" stop-opacity="0"/>
          <stop offset="0.3" stop-color="#f7a46a" stop-opacity="0.3"/>
          <stop offset="0.62" stop-color="#f2600f" stop-opacity="0.55"/>
          <stop offset="0.85" stop-color="#f7a46a" stop-opacity="0.4"/>
          <stop offset="1" stop-color="#f7a46a" stop-opacity="0"/>
        </linearGradient>
      </defs>
      <ellipse cx="560" cy="230" rx="620" ry="70" fill="#fbd2b0" opacity="0.25" filter="url(#haze-blur)"/>
      <path d="M0 200 C 260 225, 520 250, 760 256 S 1040 262, 1130 272 L 1130 286 C 1000 278, 820 274, 620 270 S 180 238, 0 214 Z"
            fill="url(#upper-trail)" filter="url(#trail-blur)"/>
      <path d="M300 330 C 520 330, 760 334, 1000 338 S 1110 342, 1160 346 L 1160 358 C 1000 354, 760 350, 520 348 S 360 344, 300 342 Z"
            fill="url(#lower-trail)" filter="url(#trail-blur)"/>
    </svg>

    <div class="wordmark">
      <h1 class="brand-name">Bright Marrow</h1>
      <p class="tagline">Clear leadership thinking for full calendars</p>
    </div>

    <div class="bloom" role="img" aria-label="Photograph of a single open cream-white rose with a pale yellow centre, softly glowing"></div>
  </div>
</body>
</html>
```